Brightpath Dentistry - Flyer - Modern & Eye catching campaign flyer

Need front & back side full page flyer designs for both 1) Grand opening 2) On-going campaign.

Attached the new dental office logo.
Attached our other dental clinic flyer designs for content.

Target Market(s)

Cosmetic dentistry

Industry/Entity Type

Health Care

Requirements
Must have
• decent, modern and eye catching marketing flyers.
Nice to have
• - Nice space
• - Highlight phone number
• - Highlight special features like convenient hours, call or text, for all ages, digital facility, etc
Should not have
• - Don't want to fill the flyer with too much wordings
• - Too many colors

```html
<!DOCTYPE html>
<html lang="en">
<head>
<meta charset="utf-8">
<title>Brightpath Dentistry – Grand Opening Flyer</title>
<link href="https://fonts.googleapis.com/css2?family=Montserrat:wght@400;500;600;700&display=swap" rel="stylesheet">
<style>
:root{
  --teal:#1fb3dc;
  --teal-bright:#00b0d8;
  --slate:#5f7a98;
  --slate-text:#6a7b92;
  --cell-1:#627b98;
  --cell-2:#7589a5;
  --cell-3:#8a9cb5;
  --header:#95a3b8;
  --white:#ffffff;
}
*{margin:0;padding:0;box-sizing:border-box}
html,body{width:849px;height:1200px;overflow:hidden;background:var(--white)}
body{font-family:'Montserrat',sans-serif;position:relative}
.flyer{position:relative;width:849px;height:1200px}

.contact{position:absolute;left:77px;top:105px;display:flex;align-items:center}
.contact__icon{width:44px;height:56px;margin-right:17px}
.contact__label{font-size:19.5px;font-weight:600;color:var(--slate);letter-spacing:1.2px;line-height:1}
.contact__number{font-size:32px;font-weight:700;color:var(--teal);letter-spacing:1px;line-height:1;margin-top:8px}
.header-divider{position:absolute;left:424px;top:101px;width:1.5px;height:64px;background:var(--slate)}

.brand{position:absolute;left:458px;top:106px;display:flex;align-items:center}
.brand__dot{width:46px;height:46px;border-radius:50%;background:var(--teal);margin-right:14px}
.brand__name{font-size:25px;font-weight:700;color:var(--teal);line-height:1.05;letter-spacing:1px;text-transform:uppercase}

.hero-photo{position:absolute;left:21px;top:170px;width:806px;height:380px;
  background:radial-gradient(ellipse at 55% 55%,#e6cdb8 0%,#d9b89c 30%,#b9c4cc 60%,#f4f6f8 100%)}

.specials{position:absolute;left:21px;top:550px;width:806px;height:105px;background:linear-gradient(90deg,#3db5dd,#22acd9 55%,#3ab7df)}
.specials__title{position:absolute;left:0;width:460px;top:18px;text-align:center;color:var(--white);font-weight:700;font-size:30px;line-height:37px;letter-spacing:2px}
.specials__title span{display:block;font-weight:600;letter-spacing:1.5px}
.specials__arrow{position:absolute;left:414px;top:21px}
.specials__list{position:absolute;left:470px;top:14px;list-style:none;color:var(--white);font-size:16px;letter-spacing:.7px;white-space:nowrap}
.specials__list li{height:28px;line-height:28px;display:flex;align-items:center}
.specials__list li::before{content:"";width:10px;height:10px;border-radius:50%;background:#d6e3ea;margin-right:9px;flex:none}
.specials__list b{font-weight:700;margin-right:6px}

.services{position:absolute;left:77px;top:670px;width:695px}
.services__head{height:46px;background:var(--header);color:var(--white);text-align:center;font-size:24px;font-weight:600;letter-spacing:2.5px;line-height:48px}
.services__grid{display:grid;grid-template-columns:232px 232px 231px;margin-top:2px;row-gap:1.5px;background:#fff}
.service{height:79px;display:flex;align-items:center;color:var(--white);font-size:14px;font-weight:500;letter-spacing:1.4px;line-height:17px;text-transform:uppercase;white-space:nowrap}
.service:nth-child(3n+1){background:var(--cell-1)}
.service:nth-child(3n+2){background:var(--cell-2)}
.service:nth-child(3n){background:var(--cell-3)}
.service svg{width:42px;height:42px;margin:0 21px 0 20px;flex:none}
.service small{display:block;text-transform:none;font-weight:400;letter-spacing:.8px;font-size:13px}

.hours{position:absolute;left:77px;top:970px;width:695px;height:46px;background:var(--teal-bright);color:var(--white);text-align:center;line-height:46px;font-size:17.5px;font-weight:600;letter-spacing:2px}
.validity{position:absolute;left:0;width:849px;top:1022px;text-align:center;color:var(--slate-text);font-size:16.5px;font-weight:600;letter-spacing:.5px}
.welcome{position:absolute;left:0;width:849px;top:1052px;text-align:center;color:var(--teal-bright);font-size:23.5px;font-weight:700;letter-spacing:2px}

.footer{position:absolute;left:21px;top:1091px;width:806px;height:53px;background:var(--slate);color:var(--white);font-size:15.5px;font-weight:500;letter-spacing:1.1px;white-space:nowrap}
.footer__item{position:absolute;top:0;height:53px;display:flex;align-items:center}
.footer__item svg{margin-right:12px;flex:none}
.footer__web{left:56px}
.footer__mail{right:44px}
.footer__divider{position:absolute;left:403px;top:12px;width:1.5px;height:30px;background:var(--teal)}
</style>
</head>
<body>
<main class="flyer">
  <svg width="0" height="0" style="position:absolute">
    <symbol id="tooth" viewBox="0 0 44 44">
      <path d="M12 6c4-2 7 1 10 1s6-3 10-1c5 3 5 11 2 17-2 4-2 15-5 15s-3-10-7-10-4 10-7 10-3-11-5-15C7 17 7 9 12 6z" fill="none" stroke="#fff" stroke-width="2.6" stroke-linejoin="round"/>
    </symbol>
  </svg>

  <header>
    <div class="contact">
      <svg class="contact__icon" viewBox="0 0 44 56" aria-hidden="true">
        <path d="M12 3l6 13-6 5c3 9 8 17 15 23l6-4 9 10-6 5C20 56 2 30 3 10z" fill="none" stroke="#5f7a98" stroke-width="4.5" stroke-linejoin="round"/>
      </svg>
      <div>
        <p class="contact__label">Call or Text Us Now:</p>
        <p class="contact__number">555.014.2273</p>
      </div>
    </div>
    <div class="header-divider"></div>
    <div class="brand">
      <div class="brand__dot"></div>
      <p class="brand__name">Brightpath<br>Dentistry</p>
    </div>
  </header>

  <div class="hero-photo" role="img" aria-label="Smiling family of four: mother, father and two children posing together"></div>

  <section class="specials">
    <h1 class="specials__title">GRAND OPENING<span>Specials</span></h1>
    <svg class="specials__arrow" width="22" height="64" viewBox="0 0 22 64" aria-hidden="true"><path d="M0 0L22 32 0 64z" fill="#cde9f4"/></svg>
    <ul class="specials__list">
      <li><b>FREE</b> Kids Dental Screening</li>
      <li><b>$25</b> Adults Dental Screening</li>
      <li><b>15% OFF</b> on Treatment Plan</li>
    </ul>
  </section>

  <section class="services">
    <h2 class="services__head">OUR SERVICES</h2>
    <div class="services__grid">
      <div class="service"><svg><use href="#tooth"/></svg><span>Root Canal<br>Therapy</span></div>
      <div class="service"><svg><use href="#tooth"/></svg><span>Dentures</span></div>
      <div class="service"><svg><use href="#tooth"/></svg><span>ClearFit<small>(Invisible braces)</small></span></div>
      <div class="service"><svg><use href="#tooth"/></svg><span>Lumen Teeth<br>Whitening</span></div>
      <div class="service"><svg><use href="#tooth"/></svg><span>Implants</span></div>
      <div class="service"><svg><use href="#tooth"/></svg><span>Night Guards</span></div>
      <div class="service"><svg><use href="#tooth"/></svg><span>Extractions</span></div>
      <div class="service"><svg><use href="#tooth"/></svg><span>Veneers</span></div>
      <div class="service"><svg><use href="#tooth"/></svg><span>Crown and<br>Bridge</span></div>
    </div>
  </section>

  <p class="hours">CONVENIENT EVENING &amp; SATURDAY HOURS</p>
  <p class="validity">Opening special offers valid until June 15, 2017 by Appointment only</p>
  <p class="welcome">NEW PATIENTS ARE WELCOME!</p>

  <footer class="footer">
    <div class="footer__item footer__web">
      <svg width="22" height="22" viewBox="0 0 22 22" aria-hidden="true"><circle cx="11" cy="11" r="9.5" fill="none" stroke="#1fb3dc" stroke-width="2"/><path d="M2 11h18M11 1.5c-5 5-5 14 0 19M11 1.5c5 5 5 14 0 19" fill="none" stroke="#1fb3dc" stroke-width="1.6"/></svg>
      <span>www.BrightpathDental.com</span>
    </div>
    <div class="footer__divider"></div>
    <div class="footer__item footer__mail">
      <svg width="22" height="15" viewBox="0 0 22 15" aria-hidden="true"><rect x="1" y="1" width="20" height="13" fill="none" stroke="#1fb3dc" stroke-width="2"/><path d="M1 1l10 8 10-8" fill="none" stroke="#1fb3dc" stroke-width="2"/></svg>
      <span>hello@BrightpathDental.com</span>
    </div>
  </footer>
</main>
</body>
</html>
```